Business card for our large format printing and installation business

We want a professional looking business card for our business. We manufacture and install Signs.

On the back of the card add this info
Large Format Graphics Printing & Installations, Event Graphics, Banners, Posters, Vehicle Fleet Graphics, Boat Wraps, Wall Murals, Decals,Displays,Signs,Plaques,Digital Signs

On the Front of the card add the Tallowfern Signs logo, plus On the back of the card add the Orange Tallowfern Wraps logo. The 2 vector logos are attached to the design brief.

Target Market(s)

Local business owners

Contact Information for Business Card

Colors
f37122
f68d4e
f9ba93

Requirements
Must have
• On the Front of the card add the Tallowfern Signs logo, plus On the back of the card add the Orange Tallowfern Wraps logo. The 2 vector logos are attached to the design brief.

```html
<!DOCTYPE html>
<html lang="en">
<head>
<meta charset="utf-8">
<title>Tallowfern Signs – Business Card</title>
<link href="https://fonts.googleapis.com/css2?family=Lato:wght@400;700;900&display=swap" rel="stylesheet">
<style>
  :root {
    --backdrop: #dcdcdc;
    --card-light: #f8f7f3;
    --card-dark: #1e1d1c;
    --brand-gold: #f6a51c;
    --brand-orange: #f37122;
    --ink: #2a2a2a;
    --ink-soft: #c9c6c0;
  }
  * { box-sizing: border-box; margin: 0; padding: 0; }
  html, body {
    width: 1200px; height: 787px; overflow: hidden;
    background: var(--backdrop);
    font-family: "Lato", Arial, sans-serif;
  }
  .sheet {
    width: 1200px; height: 787px;
    display: flex; align-items: center; justify-content: center; gap: 40px;
  }
  .card {
    width: 540px; height: 309px;
    position: relative;
    box-shadow: 0 4px 14px rgba(0,0,0,0.18);
  }
  /* Front */
  .card--front { background: var(--card-light); color: var(--ink); }
  .front-logo {
    position: absolute; left: 34px; top: 118px; width: 200px;
    font-weight: 900; font-size: 32px; line-height: 1.05;
    color: var(--brand-gold); text-align: center;
  }
  .front-divider {
    position: absolute; left: 262px; top: 60px; width: 2px; height: 190px;
    background: var(--brand-gold);
  }
  .contact {
    position: absolute; left: 290px; top: 66px; width: 235px;
    font-size: 13px; line-height: 1.45;
  }
  .contact__name {
    font-weight: 700; font-size: 17px; letter-spacing: 0.5px;
    color: var(--brand-gold); text-transform: uppercase;
  }
  .contact__role { font-size: 14px; margin-bottom: 8px; }
  .contact__address { margin-bottom: 8px; }
  .contact__line { display: flex; align-items: center; gap: 7px; }
  .contact__line svg { width: 12px; height: 12px; flex: none; fill: var(--brand-gold); }
  /* Back */
  .card--back {
    background: var(--card-dark);
    display: flex; flex-direction: column; align-items: center; justify-content: center;
    text-align: center; gap: 26px;
  }
  .back-logo {
    font-weight: 900; font-size: 40px; line-height: 1;
    color: var(--brand-gold);
  }
  .services {
    color: var(--ink-soft); font-size: 12.5px; line-height: 1.6;
  }
</style>
</head>
<body>
<main class="sheet">
  <section class="card card--front" aria-label="Card front">
    <div class="front-logo">Tallowfern Signs</div>
    <div class="front-divider"></div>
    <div class="contact">
      <p class="contact__name">Dorian Welk</p>
      <p class="contact__role">Owner</p>
      <p class="contact__address">2218 Larkmoor Avenue, Fenbrook<br>NC 4, United States</p>
      <p class="contact__line">
        <svg viewBox="0 0 24 24" aria-hidden="true"><path d="M6.6 10.8a15 15 0 0 0 6.6 6.6l2.2-2.2a1 1 0 0 1 1-.25 11.4 11.4 0 0 0 3.6.57 1 1 0 0 1 1 1V20a1 1 0 0 1-1 1A17 17 0 0 1 3 4a1 1 0 0 1 1-1h3.5a1 1 0 0 1 1 1c0 1.25.2 2.45.57 3.6a1 1 0 0 1-.25 1z"/></svg>
        000-000-000-000
      </p>
      <p class="contact__line">
        <svg viewBox="0 0 24 24" aria-hidden="true"><path d="M6 2h12v6H6zM4 9h16a2 2 0 0 1 2 2v6h-4v5H6v-5H2v-6a2 2 0 0 1 2-2zm4 8v3h8v-3z"/></svg>
        000-000-000-000
      </p>
      <p class="contact__line">
        <svg viewBox="0 0 24 24" aria-hidden="true"><path d="M2 5h20v14H2zm2 2v.5l8 5 8-5V7z"/></svg>
        info@tallowfernsigns.com
      </p>
      <p class="contact__line">
        <svg viewBox="0 0 24 24" aria-hidden="true"><path d="M12 2a10 10 0 1 0 0 20 10 10 0 0 0 0-20zm0 2c.9 0 2.2 1.8 2.7 5H9.3C9.8 5.8 11.1 4 12 4zM4.3 11h3A16 16 0 0 0 7.5 15H5a8 8 0 0 1-.7-4zm12.4 0h3a8 8 0 0 1-.7 4h-2.5a16 16 0 0 0 .2-4zM9.2 11h5.6a14 14 0 0 1-.2 4H9.4a14 14 0 0 1-.2-4z"/></svg>
        www.tallowfernsigns.com
      </p>
    </div>
  </section>

  <section class="card card--back" aria-label="Card back">
    <div class="back-logo">Tallowfern Wraps</div>
    <p class="services">
      Large Format Graphics Printing &amp; Installations, Event Graphics, Banners, Posters<br>
      Vehicle Fleet Graphics, Boat Wraps, Wall Murals, Decals<br>
      Displays, Signs, Plaques, Digital Signs
    </p>
  </section>
</main>
</body>
</html>
```